" Dinâmica, tradicional pois tem 55 anos de atuação, trabalhamos com gestão do patrimônio e comercialização de imóveis, queremos passar uma imagem de corporativismo e total seriedade. Destaque no mercado. Nossa empresa é lidar em seu seguimento. "

```html
<!DOCTYPE html>
<html lang="pt-BR">
<head>
<meta charset="UTF-8">
<title>Papel timbrado — Alicerce Patrimonial</title>
<link href="https://fonts.googleapis.com/css2?family=Open+Sans:wght@400;600;700&display=swap" rel="stylesheet">
<style>
  :root {
    --navy: #2f3183;
    --red: #d3242c;
    --ink: #5a5d66;
    --muted: #8a8d96;
    --paper: #ffffff;
    --backdrop: #e9eaef;
  }
  * { box-sizing: border-box; margin: 0; padding: 0; }
  html, body { width: 1200px; height: 1200px; overflow: hidden; }
  body {
    background: var(--backdrop);
    font-family: "Open Sans", Arial, sans-serif;
    display: flex; align-items: center; justify-content: center;
  }
  .letterhead {
    position: relative;
    width: 780px; height: 1100px;
    background: var(--paper);
    box-shadow: 0 10px 30px rgba(40, 42, 90, 0.18);
    padding: 48px 78px 0;
  }
  .brand {
    display: flex; align-items: center; justify-content: center; gap: 10px;
    color: var(--navy); font-weight: 600; font-size: 20px; letter-spacing: 0.3px;
  }
  .brand-square { width: 18px; height: 18px; background: var(--red); }
  .letter-body {
    margin-top: 78px;
    color: var(--ink); font-size: 11.5px; line-height: 1.85; text-align: justify;
  }
  .letter-body p { margin-bottom: 18px; }
  .signature {
    position: absolute; left: 450px; top: 470px; width: 240px; text-align: center;
  }
  .signature-mark {
    display: block; width: 200px; height: 46px; margin: 0 auto 6px;
    background: linear-gradient(90deg, rgba(60,62,80,0.05), rgba(60,62,80,0.14), rgba(60,62,80,0.05));
    border-radius: 4px;
  }
  .signature-name {
    border-top: 1px solid #c9cbd2; padding-top: 5px;
    font-size: 9px; letter-spacing: 1.5px; text-transform: uppercase; color: var(--muted);
  }
  .contacts {
    position: absolute; left: 78px; right: 78px; top: 918px;
    display: flex; flex-direction: column; align-items: center; gap: 9px;
    font-size: 11px; color: var(--ink); font-style: normal;
  }
  .contact-row { display: flex; gap: 28px; }
  .contact-item { display: flex; align-items: center; gap: 7px; }
  .contact-icon {
    width: 16px; height: 16px; border-radius: 3px; background: var(--red);
    display: flex; align-items: center; justify-content: center;
  }
  .rule { position: absolute; left: 0; right: 0; height: 2px; }
  .rule-red { top: 1000px; background: var(--red); }
  .rule-navy { top: 1012px; background: var(--navy); height: 3px; }
  .footer-band {
    position: absolute; left: 0; right: 0; bottom: 0; height: 62px;
    background: var(--navy); color: #fff;
    display: flex; align-items: center; justify-content: center;
    font-size: 13px; font-weight: 600; letter-spacing: 1px;
  }
</style>
</head>
<body>
  <main class="letterhead">
    <header class="brand">
      <span class="brand-square"></span>
      <span class="brand-name">Alicerce Patrimonial</span>
    </header>

    <section class="letter-body">
      <p>Há mais de cinco décadas atuamos na gestão de patrimônio e na comercialização de imóveis, sempre com seriedade, transparência e compromisso com cada cliente. Nossa equipe acompanha de perto todas as etapas de cada negociação, oferecendo segurança jurídica, avaliação criteriosa e atendimento personalizado para proprietários, investidores e famílias que buscam o imóvel ideal em toda a cidade.</p>
      <p>Acreditamos que a confiança construída ao longo dos anos é o nosso maior patrimônio. Por isso, mantemos processos claros e relatórios periódicos sobre cada imóvel administrado.</p>
      <p>Colocamo-nos à disposição para apresentar nossas soluções em administração de locações, vendas e avaliações, com a agilidade que o mercado exige e a tradição que nos distingue. Será um prazer agendar uma reunião em nosso escritório ou no local de sua preferência.</p>
      <p>Agradecemos a atenção e aguardamos o seu contato para darmos início a uma parceria duradoura e de resultados.</p>
    </section>

    <div class="signature">
      <span class="signature-mark" role="img" aria-label="Assinatura manuscrita"></span>
      <div class="signature-name">Renata Albuquerque</div>
    </div>

    <address class="contacts">
      <div class="contact-row">
        <span class="contact-item">
          <span class="contact-icon">
            <svg width="10" height="10" viewBox="0 0 24 24"><path fill="#fff" d="M6.6 10.8a15 15 0 0 0 6.6 6.6l2.2-2.2a1 1 0 0 1 1-.25 11.4 11.4 0 0 0 3.6.57 1 1 0 0 1 1 1V20a1 1 0 0 1-1 1A17 17 0 0 1 3 4a1 1 0 0 1 1-1h3.5a1 1 0 0 1 1 1c0 1.25.2 2.45.57 3.6a1 1 0 0 1-.25 1z"/></svg>
          </span>
          11 3200-4400
        </span>
        <span class="contact-item">
          <span class="contact-icon">
            <svg width="10" height="10" viewBox="0 0 24 24"><path fill="#fff" d="M3 5h18v14H3z M3 5l9 7 9-7" stroke="#d3242c" stroke-width="1.6"/></svg>
          </span>
          contato@alicercepatrimonial.com.br
        </span>
      </div>
      <span class="contact-item">
        <span class="contact-icon">
          <svg width="10" height="10" viewBox="0 0 24 24"><path fill="#fff" d="M12 2a7 7 0 0 0-7 7c0 5 7 13 7 13s7-8 7-13a7 7 0 0 0-7-7zm0 9.5A2.5 2.5 0 1 1 12 6.5a2.5 2.5 0 0 1 0 5z"/></svg>
        </span>
        Avenida Almeida Prado, 820 - Centro - São Paulo/SP
      </span>
    </address>

    <div class="rule rule-red"></div>
    <div class="rule rule-navy"></div>
    <footer class="footer-band">www.alicercepatrimonial.com.br</footer>
  </main>
</body>
</html>
```